Coastline Wing Flights brochure

A single A4 brochures that is tri-folded and shows some of our tour packages with contact details.

Please visit www.coastlinewingflights.com.au to see the designs and images that can be used.

I want to provide designers the freedom to try something creative because I want to give prospective client - normally tourists to Sydney a quality service. I want the brochure to reflect this.

The image on the front page needs to be of the Sydney Harbour. The image MUST be in daylight - not night time.

I have now provided an image of the aircraft (in GIF format). Please use this image and place it over the image of the sydney harbour bridge and sydney opera house.

I may need to discuss this further but what I have not show in the attached files is a small form I will like the client to fill out..

Reservation number
Name
Address
Phone number
Email

We can discuss this at a latter time.

The QR Code needs to contain your web address (www.coastlinewingflights.com.au)

Target Market(s)

Visitors and tourists to Sydney who want a day trip.
We are providing an exciting way to see Sydney. By air in a light aircraft...

Font styles to use
Sans Serif
Script

Colors
33a6d7
3276b5
85acd3
85cae6
ffffff

Requirements
Must have
• Brochure must be A4 (with about 2 to 3mm bleed - so it can be cut at the printers). They but be folded in 3 to produce a DL size brochure.

The words "Prepare to be amazed" should be in script font...

Please use the following wording for our Terms can conditions...

Terms and Conditions
Coastline Wing Flights operates from Marrowvale Airfield within Sydney’s busy airspace Your chosen flight may be subject to delays. Clearance to enter controlled airspace may be refused - this is especially true of our popular Tidewater Vista flight. If this happens, we can either offer other suitable flights, reschedule the flight or, if this isn’t suitable, we provide a refund.
Other aircraft, besides our standard Falcrest Ranger, are available if we consider they better suit your requirements.
See our web site www.coastlinewingflights.com.au for full details.
Coastline Wing Flights is a trading name of Quorvex Pty Limited
(ABN 81 417 266 905) which operates under the Air Operators Certificate (AOC) of Drummond and Pettigrew Pty Ltd.
Nice to have
• Suggestion - on one of the sides (with the packages) to have a background image.

Suggestion is to keep the brochure light and "airy"

```html
<!DOCTYPE html>
<html lang="en">
<head>
<meta charset="utf-8">
<title>Coastline Wing Flights – Tour Packages</title>
<link href="https://fonts.googleapis.com/css2?family=Open+Sans:wght@300;400;600&family=Satisfy&display=swap" rel="stylesheet">
<style>
  :root {
    --ink: #000000;
    --white: #ffffff;
    --blue-deep: #3276b5;
    --blue-mid: #33a6d7;
    --blue-soft: #85acd3;
    --blue-pale: #85cae6;
    --paper-light: #fbfbfb;
    --paper-shade: #e4e4e4;
    --text: #111111;
  }
  * { box-sizing: border-box; margin: 0; padding: 0; }
  html, body { width: 1200px; height: 849px; overflow: hidden; background: var(--white); }
  .brochure {
    position: relative; width: 1200px; height: 849px; overflow: hidden;
    font-family: "Open Sans", Arial, sans-serif; color: var(--text);
    background: linear-gradient(90deg, var(--paper-shade) 0%, var(--paper-light) 22%, var(--paper-shade) 34%, var(--paper-light) 55%, var(--paper-shade) 68%, var(--paper-light) 85%, var(--paper-shade) 100%);
  }
  .intro-band {
    position: absolute; top: 0; left: 0; width: 1200px; height: 103px; background: var(--ink);
    display: flex;
  }
  .intro-band p {
    width: 400px; padding: 16px 16px 0; text-align: center;
    font-family: "Satisfy", cursive; color: var(--white); font-size: 13.3px; line-height: 18.5px;
  }
  .rule { position: absolute; top: 106px; left: 0; width: 1200px; height: 2px; background: var(--ink); }
  .hero { position: absolute; top: 113px; left: 0; width: 1200px; height: 320px; }
  .meta { position: absolute; top: 446px; font-size: 14.5px; line-height: 23px; color: var(--blue-deep); list-style: none; white-space: nowrap; }
  .meta li { display: flex; align-items: center; gap: 5px; }
  .meta strong { font-weight: 600; }
  .meta svg { width: 12px; height: 12px; flex: none; }
  .meta--1 { left: 159px; } .meta--2 { left: 576px; } .meta--3 { left: 984px; }
  .tour-title {
    position: absolute; top: 522px; height: 30px; background: var(--ink); color: var(--white);
    font-size: 17px; line-height: 30px; font-weight: 300; white-space: nowrap;
  }
  .tour-title--1 { left: 0; width: 209px; padding-left: 22px; }
  .tour-title--2 { left: 400px; width: 151px; padding-left: 26px; }
  .tour-title--3 { left: 801px; width: 189px; padding-left: 26px; }
  .stops { position: absolute; top: 571px; list-style: none; font-size: 14.5px; line-height: 21.4px; white-space: nowrap; }
  .stops li { position: relative; padding-left: 18px; }
  .stops li::before {
    content: ""; position: absolute; left: 0; top: 5px; width: 11px; height: 11px; background: var(--ink);
  }
  .stops li::after {
    content: ""; position: absolute; left: 3px; top: 8px; width: 5px; height: 5px;
    border-top: 1.5px solid var(--white); border-right: 1.5px solid var(--white);
  }
  .stops--1 { left: 28px; } .stops--2 { left: 428px; } .stops--3 { left: 829px; }
  .foot-band { position: absolute; left: 0; bottom: 0; width: 1200px; height: 32px; background: var(--blue-deep); }
</style>
</head>
<body>
<main class="brochure">
  <header class="intro-band">
    <p>This is one of our most popular scenic tours because it showcases Sydneys magnificent coastline and world famous beaches. The Sydney coastal flight takes you past many well known coastal land-marks and beaches such as Maroubra Beach</p>
    <p>This is one of our most popular scenic tours because it showcases Sydneys magnificent coastline and world famous beaches. The Sydney coastal flight takes you past many well known coastal land-marks and beaches such as Maroubra Beach</p>
    <p>This is one of our most popular scenic tours because it showcases Sydneys magnificent coastline and world famous beaches. The Sydney coastal flight takes you past many well known coastal land-marks and beaches such as Maroubra Beach</p>
  </header>
  <div class="rule"></div>

  <svg class="hero" viewBox="0 0 1200 320" aria-hidden="false">
    <defs>
      <path id="wave-cut" d="M0 0H1200V215C1030 235 850 275 640 250C450 225 250 215 0 235Z"/>
      <clipPath id="photo-edge"><use href="#wave-cut"/></clipPath>
      <linearGradient id="tone-harbour" x1="0" y1="0" x2="0" y2="1">
        <stop offset="0" stop-color="#9dc3e0"/><stop offset="0.3" stop-color="#5f8fa8"/><stop offset="0.55" stop-color="#2f6f78"/><stop offset="1" stop-color="#1e5a5c"/>
      </linearGradient>
      <linearGradient id="tone-beach" x1="0" y1="0" x2="0" y2="1">
        <stop offset="0" stop-color="#5aa0e0"/><stop offset="0.28" stop-color="#b9cfe0"/><stop offset="0.45" stop-color="#e6ddc8"/><stop offset="0.58" stop-color="#4b8fb4"/><stop offset="0.8" stop-color="#6d8f4d"/><stop offset="1" stop-color="#4c7a3a"/>
      </linearGradient>
      <linearGradient id="tone-cliffs" x1="0" y1="0" x2="1" y2="0">
        <stop offset="0" stop-color="#2e3a42"/><stop offset="0.25" stop-color="#b76a2e"/><stop offset="0.5" stop-color="#d98b3c"/><stop offset="0.75" stop-color="#a85b26"/><stop offset="1" stop-color="#3a4650"/>
      </linearGradient>
    </defs>
    <use href="#wave-cut" transform="translate(0 40)" fill="var(--blue-pale)"/>
    <use href="#wave-cut" transform="translate(0 30)" fill="var(--blue-soft)"/>
    <use href="#wave-cut" transform="translate(0 22)" fill="var(--blue-mid)"/>
    <use href="#wave-cut" transform="translate(0 12)" fill="var(--blue-deep)"/>
    <g clip-path="url(#photo-edge)">
      <rect width="1200" height="320" fill="var(--white)"/>
      <rect x="0" width="398" height="320" fill="url(#tone-harbour)" role="img" aria-label="Aerial view of the Sydney Harbour Bridge from a light aircraft wing"/>
      <rect x="400" width="401" height="320" fill="url(#tone-beach)" role="img" aria-label="Sunny Sydney beach with surf, sand and grassy headland"/>
      <rect x="803" width="397" height="320" fill="url(#tone-cliffs)" role="img" aria-label="Golden sandstone rock pillars of the Blue Mountains at sunset"/>
    </g>
  </svg>

  <ul class="meta meta--1">
    <li><svg viewBox="0 0 12 12"><circle cx="6" cy="6" r="5" fill="none" stroke="currentColor" stroke-width="1.2"/><path d="M6 3v3h2" fill="none" stroke="currentColor" stroke-width="1.2"/></svg><span><strong>Duration:</strong> 1 hour 20 mins</span></li>
    <li><svg viewBox="0 0 12 12"><path d="M1 1h5l5 5-5 5-5-5z" fill="currentColor"/><circle cx="3.5" cy="3.5" r="1" fill="#fff"/></svg><span><strong>Price:</strong> $560 per aircraft</span></li>
  </ul>
  <ul class="meta meta--2">
    <li><svg viewBox="0 0 12 12"><circle cx="6" cy="6" r="5" fill="none" stroke="currentColor" stroke-width="1.2"/><path d="M6 3v3h2" fill="none" stroke="currentColor" stroke-width="1.2"/></svg><span><strong>Duration:</strong> 1 hour 20 mins</span></li>
    <li><svg viewBox="0 0 12 12"><path d="M1 1h5l5 5-5 5-5-5z" fill="currentColor"/><circle cx="3.5" cy="3.5" r="1" fill="#fff"/></svg><span><strong>Price:</strong> $560 per aircraft</span></li>
  </ul>
  <ul class="meta meta--3">
    <li><svg viewBox="0 0 12 12"><circle cx="6" cy="6" r="5" fill="none" stroke="currentColor" stroke-width="1.2"/><path d="M6 3v3h2" fill="none" stroke="currentColor" stroke-width="1.2"/></svg><span><strong>Duration:</strong> 1 hour 10 mins</span></li>
    <li><svg viewBox="0 0 12 12"><path d="M1 1h5l5 5-5 5-5-5z" fill="currentColor"/><circle cx="3.5" cy="3.5" r="1" fill="#fff"/></svg><span><strong>Price:</strong> $475 per aircraft</span></li>
  </ul>

  <h2 class="tour-title tour-title--1">Tidewater Vista</h2>
  <h2 class="tour-title tour-title--2">Sydney Coastal</h2>
  <h2 class="tour-title tour-title--3">The Blue Mountains</h2>

  <ul class="stops stops--1">
    <li>Parramatta City</li>
    <li>Hornsby</li>
    <li>Bahai Temple</li>
    <li>Sydney Harbour Bridge</li>
    <li>Opera House</li>
    <li>Manly</li>
    <li>Long Reef</li>
  </ul>
  <ul class="stops stops--2">
    <li>Cambelltown</li>
    <li>Stanwell Park</li>
    <li>Entrance of Port Hacking</li>
    <li>Entrance of Botany Bay</li>
    <li>Famous Sydney Beaches including<br>Maroubra, Cooge, Bondi &amp; Manly</li>
    <li>Sydney Heads</li>
    <li>Long Reef</li>
  </ul>
  <ul class="stops stops--3">
    <li>Katoomba</li>
    <li>The Three Sisters</li>
    <li>Warragamba Dam</li>
    <li>Prospect Resrvour</li>
  </ul>

  <div class="foot-band"></div>
</main>
</body>
</html>
```